Postcard Design Project

Cleaning service for house, apartments and condominiums.
Suggested inclusions are:We know you have better things to do with your time. We offer thorough, detailed cleaning services. So simply relax and leave the house cleaning to us!
100% Work Guaranteed
Meadowlark Home Cleaning 512-739-204 Call Today!
Affordable, Reliable, Residential Cleaning Services
Enjoy a clean home without lifting a finger
www.meadowlarkhomecleaning.example
an explosive burst with “20% Off First Cleaning”
Benefits of Using our Service
We clean the places you don’t have time to clean
We use our professional equipment and supplies
We use cleaning products that are gentle on your home

Industry/Entity Type

Cleaning Service

```html
<!DOCTYPE html>
<html lang="en">
<head>
<meta charset="utf-8">
<title>Meadowlark Home Cleaning – Postcard</title>
<link rel="stylesheet" href="https://fonts.googleapis.com/css2?family=Julius+Sans+One&family=Oswald:wght@600&family=Yellowtail&family=Montserrat:wght@400;500&display=swap">
<style>
  :root {
    --page: #2b2b2d;
    --ink: #ffffff;
    --ink-soft: rgba(255,255,255,0.92);
    --night: #1c1833;
    --deep-sea: #1f5a78;
    --lagoon: #2fa9b4;
    --shallows: #9fcfc6;
    --sand: #b9c9b8;
    --frame-wood: #6b5842;
  }
  * { box-sizing: border-box; margin: 0; padding: 0; }
  html, body { width: 1200px; height: 900px; overflow: hidden; }
  body {
    background: var(--page);
    display: flex;
    align-items: center;
    justify-content: center;
    font-family: "Julius Sans One", sans-serif;
    color: var(--ink);
  }
  .postcard {
    position: relative;
    width: 560px;
    height: 840px;
    overflow: hidden;
    box-shadow: 0 10px 30px rgba(0,0,0,0.45);
  }
  .postcard__scene {
    position: absolute;
    inset: 0;
    background:
      radial-gradient(ellipse at 50% 55%, rgba(255,255,255,0.12), transparent 60%),
      linear-gradient(90deg, rgba(60,45,30,0.55), transparent 18%, transparent 82%, rgba(60,45,30,0.55)),
      linear-gradient(180deg, var(--night) 0%, #2a3a6a 14%, var(--deep-sea) 30%, var(--lagoon) 45%, var(--shallows) 62%, var(--sand) 100%);
  }
  .postcard__content {
    position: relative;
    height: 100%;
    display: flex;
    flex-direction: column;
    align-items: center;
    text-align: center;
    padding: 48px 50px 30px;
  }
  .brand-name {
    font-family: "Julius Sans One", sans-serif;
    font-size: 24px;
    letter-spacing: 2px;
    color: var(--ink);
  }
  .rule {
    width: 36px;
    height: 2px;
    background: var(--ink);
    margin: 16px auto 18px;
  }
  .bracketed {
    position: relative;
    padding: 10px 22px;
  }
  .bracketed::before,
  .bracketed::after {
    content: "";
    position: absolute;
    top: 0;
    bottom: 0;
    width: 12px;
    border: 2px solid var(--ink);
  }
  .bracketed::before { left: 0; border-right: none; }
  .bracketed::after { right: 0; border-left: none; }
  .intro {
    font-size: 15px;
    line-height: 1.45;
    text-transform: uppercase;
    letter-spacing: 0.5px;
  }
  .headline {
    font-family: "Oswald", sans-serif;
    font-weight: 600;
    font-size: 42px;
    letter-spacing: 1px;
    margin-top: 22px;
    text-shadow: 0 2px 6px rgba(0,0,0,0.3);
  }
  .tagline {
    font-size: 16px;
    line-height: 1.45;
    text-transform: uppercase;
    margin-top: 8px;
  }
  .tagline .rule { margin: 8px auto; }
  .burst-lead {
    font-family: "Montserrat", sans-serif;
    font-size: 12px;
    margin-top: 10px;
  }
  .offer {
    font-family: "Yellowtail", cursive;
    font-size: 34px;
    margin-top: 6px;
    padding: 6px 26px;
  }
  .benefits-title {
    font-size: 17px;
    text-transform: uppercase;
    margin-top: 22px;
  }
  .benefits {
    list-style: none;
    margin-top: 12px;
    font-family: "Montserrat", sans-serif;
    font-size: 12.5px;
    line-height: 1.35;
    text-align: center;
  }
  .benefits li {
    display: flex;
    align-items: flex-start;
    gap: 10px;
    margin-bottom: 8px;
    max-width: 380px;
  }
  .benefits svg { flex: none; margin-top: 2px; }
  .contact {
    margin-top: auto;
    padding: 8px 26px;
    font-family: "Montserrat", sans-serif;
  }
  .contact__name { font-size: 17px; font-weight: 400; }
  .contact__phone { font-size: 20px; font-weight: 500; margin-top: 2px; }
  .contact__web {
    font-family: "Montserrat", sans-serif;
    font-size: 13px;
    margin-top: 8px;
  }
</style>
</head>
<body>
  <article class="postcard">
    <div class="postcard__scene" role="img" aria-label="Photo of a tropical beach with turquoise sea, palm fronds and a wooden rowboat seen through an open window frame"></div>
    <div class="postcard__content">
      <div class="brand-name">Meadowlark Home Cleaning</div>
      <div class="rule"></div>
      <p class="intro bracketed">We know you have better things to do with your time. We offer thorough, detailed cleaning services. So simply relax and leave the house cleaning to us!</p>
      <h1 class="headline">100% WORK GUARANTEED</h1>
      <div class="tagline">
        <p>Affordable, Reliable, Residential<br>Cleaning Services</p>
        <div class="rule"></div>
        <p>Enjoy a clean home without lifting a finger</p>
      </div>
      <p class="burst-lead">an explosive burst with</p>
      <p class="offer bracketed">20% Off First Cleaning</p>
      <h2 class="benefits-title">Benefits of Using our Service</h2>
      <ul class="benefits">
        <li><svg width="14" height="14" viewBox="0 0 14 14"><rect x="0.5" y="0.5" width="13" height="13" fill="none" stroke="#fff"/><path d="M3 7l3 3 5-6" fill="none" stroke="#fff" stroke-width="1.5"/></svg>We clean the places you don’t have time to clean</li>
        <li><svg width="14" height="14" viewBox="0 0 14 14"><rect x="0.5" y="0.5" width="13" height="13" fill="none" stroke="#fff"/><path d="M3 7l3 3 5-6" fill="none" stroke="#fff" stroke-width="1.5"/></svg>We use our professional equipment and supplies</li>
        <li><svg width="14" height="14" viewBox="0 0 14 14"><rect x="0.5" y="0.5" width="13" height="13" fill="none" stroke="#fff"/><path d="M3 7l3 3 5-6" fill="none" stroke="#fff" stroke-width="1.5"/></svg>We use cleaning products that are gentle on your home</li>
      </ul>
      <div class="contact bracketed">
        <p class="contact__name">Meadowlark Home Cleaning</p>
        <p class="contact__phone">512-739-204 Call Today!</p>
      </div>
      <p class="contact__web">www.meadowlarkhomecleaning.example</p>
    </div>
  </article>
</body>
</html>
```